Brochure Design Project

Job Type:

1 unified, standard format for 4 marketing templates: doorhanger, factsheet, case study, tri-fold for an energy-services company (helping people and utilities save money)

Task Outline:

Generic templates for 4 marketing pieces that can be used-in other words: latin text fill, lots of pictures that can be replaced or modified, very professional and warm look, deliverable can be modified upon purchase for different programs since we participate in constantly changing programs (universal template is what we’re looking for). The 4 pieces should have a standard look and feel (i.e., same design, different size layout)

Task Description:

The templates will be used to inform/attract clients to our energy efficiency and renewable energy programs. These programs include home improvement measures that cut energy costs and can be funded by government rebate programs. Clients range from residential homeowners, small business owners, and mobile home owners (we will modify pictures, insert text upon delivery for each segment). The template will need to be professional and have the ability to be edited by our staff because we constantly have new programs forming.

Target Market(s)

Utilities, residential, mobile home, small commercial

Industry/Entity Type

Home Improvement

Requirements
Must have
• 1. Locations for the following logos:

PowerMark Ally
HTRW
QVN A+
Utility Logo
Tallwick Group
(See example here: http://www.tallwickgroup.example/index.php?option=com_content&view=article&id=148:northvale-fuel-board-manufactured-mobile-homes&catid=44&Itemid=108)

2. Location for a utility disclaimer box (see box at the bottom of the page in the link above)

3. Location for name of program at the top of the page
Nice to have
• Lots of room for pictures (e.g., see second page of this link:http://www.tallwickgroup.example/index.php?option=com_content&view=article&id=148:northvale-fuel-board-manufactured-mobile-homes&catid=44&Itemid=108 )

see also 2nd page: http://www.tallwickgroup.example/index.php?option=com_content&view=article&id=149:corrin-heat-and-light-manufactured-mobile-home-program&catid=44&Itemid=108

Front / back on 4 templates, color

```html
<!DOCTYPE html>
<html lang="en">
<head>
<meta charset="utf-8">
<title>Manufactured - Mobile Home Energy-Efficiency Program</title>
<link href="https://fonts.googleapis.com/css2?family=Arimo:ital,wght@0,400;0,700;1,400&display=swap" rel="stylesheet">
<style>
  :root {
    --sky-top: #2f8fd0;
    --sky-mid: #7cc3ec;
    --sky-low: #d7eef9;
    --grass-dark: #3d8a1f;
    --grass-light: #8cc63f;
    --header-blue: #1d6fb4;
    --header-green: #5fae3a;
    --badge-green: #4f9e2c;
    --text-white: #ffffff;
    --text-dark: #1d3550;
    --phone-blue: #0d5fa6;
    --strip-white: #ffffff;
    --fine-grey: #55606b;
  }
  * { margin: 0; padding: 0; box-sizing: border-box; }
  html, body { width: 900px; height: 1200px; overflow: hidden; background: #ffffff; }
  body { font-family: "Arimo", Arial, sans-serif; }

  .flyer { position: relative; width: 900px; height: 1200px; overflow: hidden; background: #ffffff; }

  .sky-photo {
    position: absolute; left: 0; top: 0; width: 900px; height: 1035px;
    background: linear-gradient(180deg, var(--sky-top) 0%, var(--sky-mid) 45%, var(--sky-low) 78%, #eef8e4 86%);
  }
  .grass-photo {
    position: absolute; left: 0; top: 875px; width: 900px; height: 160px;
    background: linear-gradient(180deg, rgba(140,198,63,0) 0%, var(--grass-light) 35%, var(--grass-dark) 100%);
  }
  .left-fade {
    position: absolute; left: 0; top: 0; width: 300px; height: 1035px;
    background: linear-gradient(90deg, rgba(255,255,255,0.85) 0%, rgba(255,255,255,0) 100%);
  }

  .program-bar {
    position: absolute; left: 0; top: 24px; width: 900px; height: 44px;
    background: linear-gradient(90deg, var(--header-blue) 0%, #2a86c8 60%, var(--header-green) 100%);
    display: flex; align-items: center; padding-left: 36px;
    color: var(--text-white); font-weight: 700; font-size: 18px; letter-spacing: 0.3px; white-space: nowrap;
  }

  .enjoy-badge {
    position: absolute; left: 740px; top: 80px; width: 126px; height: 126px; border-radius: 50%;
    background: radial-gradient(circle at 40% 35%, #79c44a, var(--badge-green));
    border: 3px solid #ffffff;
    display: flex; align-items: center; justify-content: center; text-align: center;
    color: var(--text-white); font-weight: 700; font-size: 12.5px; line-height: 1.25; padding: 14px;
  }

  .content { position: absolute; left: 285px; top: 112px; width: 560px; color: var(--text-white); }
  .headline { font-size: 80px; font-weight: 400; line-height: 1; }
  .subhead { margin-top: 22px; font-size: 27px; line-height: 1.25; }
  .subhead strong { font-weight: 700; }
  .intro { margin-top: 24px; font-size: 17px; line-height: 1.4; color: var(--text-dark); }
  .measures { margin-top: 14px; list-style: none; font-size: 17px; line-height: 1.45; color: var(--text-dark); }
  .measures li::before { content: "• "; }
  .note { margin-top: 18px; font-size: 12px; color: var(--text-dark); }

  .call-box {
    position: absolute; left: 285px; top: 705px; width: 510px; height: 172px;
    background: rgba(255,255,255,0.82); border-radius: 22px;
    text-align: center; color: var(--phone-blue); padding-top: 14px;
  }
  .call-lead { font-size: 22px; line-height: 1.2; }
  .call-lead strong { font-weight: 700; }
  .call-number { font-size: 44px; font-weight: 700; margin-top: 4px; line-height: 1.1; }
  .call-details { font-size: 12px; line-height: 1.35; color: var(--fine-grey); margin-top: 4px; }

  .partner-strip {
    position: absolute; left: 0; top: 1035px; width: 900px; height: 72px; background: var(--strip-white);
    display: flex; align-items: center; justify-content: space-around; padding: 0 18px;
  }
  .partner { display: flex; align-items: center; gap: 7px; font-size: 16px; font-weight: 700; color: var(--header-blue); }
  .partner-square { width: 22px; height: 22px; background: var(--header-blue); }
  .partner-circle { width: 22px; height: 22px; border-radius: 50%; background: var(--header-blue); }

  .disclaimer {
    position: absolute; left: 20px; top: 1112px; width: 860px;
    font-size: 10.5px; line-height: 1.4; color: var(--fine-grey);
  }
</style>
</head>
<body>
<div class="flyer">
  <div class="sky-photo" role="img" aria-label="Photo of a bright blue sky with soft clouds"></div>
  <div class="grass-photo" role="img" aria-label="Photo of fresh green grass"></div>
  <div class="left-fade"></div>

  <div class="program-bar">MANUFACTURED - MOBILE HOME ENERGY - EFFICIENCY PROGRAM</div>
  <div class="enjoy-badge">ENJOY A MORE ENERGY - EFFICIENT HOME !</div>

  <div class="content">
    <h1 class="headline">Act Now</h1>
    <p class="subhead">and receive energy-saving products and services at <strong>NO COST !</strong></p>
    <p class="intro">By participating in the Northvale Power/ Corrin Gas Company Manufactured- Mobile Home Energy-Efficiency Program, your home may qualify for installation for the following energy-efficient measures * at NO COST at you.</p>
    <ul class="measures">
      <li>Air Duct Leakage Testing and Sealing</li>
      <li>Compact Florescent Light Bulbs</li>
      <li>Hard-wired Compact Florescent Light Fixtures</li>
      <li>Low-flow Showerheads and Faucet Aerators</li>
      <li>Pipe-wrap</li>
    </ul>
    <p class="note">*Not all homes will qualify for all measures.</p>
  </div>

  <div class="call-box">
    <p class="call-lead">Call today for more Energy-Efficient<br>home at <strong>NO COST</strong> to you!</p>
    <p class="call-number">888-555-0147</p>
    <p class="call-details">Monday - Friday 8 a.m. - 5 p.m.<br>www.tallwickgroup.example<br>State Contractor License #882104</p>
  </div>

  <div class="partner-strip">
    <div class="partner"><span class="partner-square"></span>PowerMark Ally</div>
    <div class="partner">HTRW</div>
    <div class="partner"><span class="partner-square"></span>QVN A+</div>
    <div class="partner">Northvale</div>
    <div class="partner">Corrin Gas</div>
    <div class="partner"><span class="partner-circle"></span>Tallwick Group</div>
  </div>

  <p class="disclaimer">Northvale Power and Corrin Gas Company provide this program to qualified customers in their service territories. Measures are installed by licensed contractors at no cost to eligible households. Availability is limited and subject to change without notice. Program funds are provided by utility customers and administered under the oversight of the state public utilities commission.</p>
</div>
</body>
</html>
```